Create a Magazine Ad for an asbestos law firm

we need an 8 X 13 ad to be on the back of a magazine cover. We have the text Attached and want a similar look and feel to our website : www.harborvale-claims.example. The ad should be targeted to white males 55 years or older who are conservative and worked in industry or industrial plants. The main offer is a free case review and trying to get them to call the telephone number.

Target Market(s)

White collar men who worked in industrial plants. Age 55 years or older.

Industry/Entity Type

Legal

Requirements
Must have
• Pictures of white middle class conservative man or man and woman
Nice to have
• look at www.harborvale-claims.example to an. idea of what we are looking for

```html
<!DOCTYPE html>
<html lang="en">
<head>
<meta charset="UTF-8">
<title>Mesothelioma &amp; Asbestos Compensation – Magazine Ad</title>
<link href="https://fonts.googleapis.com/css2?family=Montserrat:wght@500;600;700;800&family=Poppins:wght@400;500;600;700;800&display=swap" rel="stylesheet">
<style>
  :root {
    --navy: #1f2a5c;
    --navy-deep: #0c1445;
    --ink: #0f1548;
    --gold: #f5d000;
    --cream: #faf6dc;
    --cream-deep: #f6f0c4;
    --grey: #55596a;
    --white: #ffffff;
  }
  * { margin: 0; padding: 0; box-sizing: border-box; }
  html, body { width: 914px; height: 1200px; overflow: hidden; background: var(--white); }
  .ad { position: relative; width: 914px; height: 1200px; overflow: hidden; font-family: "Poppins", sans-serif; }

  /* Header */
  .hero { position: absolute; left: 0; top: 0; width: 914px; height: 317px; }
  .hero-photo { position: absolute; inset: 0; background: linear-gradient(180deg, #2a3566 0%, #34416f 55%, #2b3868 75%, #1e2a5a 100%); }
  .hero-title { position: absolute; left: 73px; top: 27px; font-family: "Montserrat", sans-serif; font-weight: 500; font-size: 54px; line-height: 65px; color: var(--white); letter-spacing: 0.2px; white-space: nowrap; }
  .hero-subtitle { position: absolute; left: 74px; top: 161px; font-family: "Montserrat", sans-serif; font-weight: 500; font-size: 21.5px; color: var(--gold); white-space: nowrap; }
  .exposure-list { position: absolute; left: 74px; top: 204px; width: 800px; font-family: "Montserrat", sans-serif; font-weight: 500; font-size: 15px; color: var(--white); }
  .exposure-list .row { display: flex; height: 29.5px; align-items: center; white-space: nowrap; }
  .exposure-list span::before { content: "•"; margin-right: 10px; }
  .exposure-list span { margin-right: 17px; }
  .gold-rule { position: absolute; left: 0; top: 317px; width: 914px; height: 14px; background: var(--gold); }

  /* Body sections */
  .heading { position: absolute; font-family: "Montserrat", sans-serif; font-weight: 700; color: var(--ink); font-size: 23px; white-space: nowrap; }
  .points { position: absolute; left: 74px; list-style: none; font-size: 15px; color: var(--grey); font-weight: 500; }
  .points li { height: 23.5px; display: flex; align-items: center; }
  .points li::before { content: "•"; width: 24px; font-size: 14px; }

  .veteran-text { position: absolute; left: 70px; top: 626px; width: 508px; font-size: 16px; line-height: 19.2px; color: var(--grey); text-align: justify; }
  .veteran-photo-shadow { position: absolute; left: 629px; top: 608px; width: 214px; height: 136px; background: var(--navy-deep); }
  .veteran-photo { position: absolute; left: 619px; top: 591px; width: 217px; height: 145px; background: linear-gradient(180deg, #a9c0d6 0%, #d8dde2 45%, #f2f2f0 70%, #cfd3d8 100%); }

  .recoveries-note { position: absolute; left: 70px; top: 761px; font-family: "Montserrat", sans-serif; font-weight: 600; font-size: 15px; color: var(--ink); }

  .results-band { position: absolute; left: 0; top: 786px; width: 914px; height: 199px; background: var(--cream); }
  .results-band::after { content: ""; position: absolute; left: 282px; top: 165px; width: 632px; height: 34px; background: var(--cream-deep); }
  .results { position: absolute; left: 68px; top: 801px; width: 778px; height: 169px; border: 2px solid var(--navy-deep); border-collapse: collapse; z-index: 1; table-layout: fixed; }
  .results td { border: 2px solid var(--navy-deep); text-align: center; vertical-align: middle; }
  .results .amount { display: block; font-family: "Montserrat", sans-serif; font-weight: 700; font-size: 21px; color: var(--ink); line-height: 26px; }
  .results .source { display: block; font-family: "Montserrat", sans-serif; font-weight: 600; font-size: 15px; color: var(--grey); line-height: 19px; margin-top: 6px; }

  /* Footer */
  .footer { position: absolute; left: 0; top: 985px; width: 914px; height: 215px; background: linear-gradient(180deg, #2c3569 0%, #3a4275 100%); }
  .footer-flag { position: absolute; left: 0; top: 0; width: 300px; height: 215px; background: linear-gradient(90deg, rgba(140,60,80,0.25) 0%, rgba(58,66,117,0) 100%); }
  .promise { position: absolute; left: 70px; top: 1004px; width: 780px; font-size: 18.5px; line-height: 23px; color: var(--white); font-weight: 500; }
  .promise strong { color: var(--gold); font-weight: 800; }
  .call-now { position: absolute; left: 188px; top: 1067px; display: flex; align-items: center; gap: 14px; font-family: "Poppins", sans-serif; font-weight: 700; font-size: 38px; color: var(--white); white-space: nowrap; }
  .call-now .number { color: var(--gold); }
  .call-now svg { width: 30px; height: 30px; }
  .consult-rule { position: absolute; left: 200px; top: 1127px; width: 249px; height: 3px; background: var(--white); }
  .consult { position: absolute; left: 471px; top: 1110px; font-weight: 700; font-size: 26px; color: var(--white); }
  .sponsor { position: absolute; left: 198px; top: 1145px; font-size: 22px; color: var(--white); font-weight: 500; white-space: nowrap; }
  .sponsor strong { color: var(--gold); font-weight: 800; }
</style>
</head>
<body>
<main class="ad">
  <header class="hero">
    <div class="hero-photo" role="img" aria-label="Navy cutter ship in harbour under a blue tint"></div>
    <h1 class="hero-title">MESOTHELIOMA &amp;<br>ASBESTOS COMPENSATION</h1>
    <p class="hero-subtitle">COMMON ASBESTOS EXPOSURE THAT CAUSES MESOTHELIOMA</p>
    <div class="exposure-list">
      <div class="row"><span>CONSTRUCTION</span><span>SHIPYARD</span><span>AUTOMOTIVE</span><span>INDUSTRIAL</span><span>PLUMBERS</span><span>PIPEFITTERS</span></div>
      <div class="row"><span>MINERS</span><span>INSULATORS</span><span>RAILROAD</span><span>NAVY</span><span>POWER PLANTS</span><span>WASHING CLOTHES</span></div>
      <div class="row"><span>TEXTILE</span><span>SECOND HAND EXPOSURE FROM SPOUSE</span><span>R&amp;H TALCUM POWDER / BABY POWDER</span></div>
    </div>
  </header>
  <div class="gold-rule"></div>

  <h2 class="heading" style="left:73px; top:341px;">CALL 1 800 555-0148 FOR A FREE CONSULTATION</h2>
  <ul class="points" style="top:373px;">
    <li>CALCULATE HOW MUCH YOU MAY BE OWED</li>
    <li>FILE YOUR MESOTHELIOMA CLAIM TODAY</li>
    <li>REPRESENTATIVES AVAILABLE 24/7</li>
  </ul>

  <h2 class="heading" style="left:73px; top:462px;">NATIONWIDE ASSISTANCE</h2>
  <ul class="points" style="top:497px;">
    <li>OVER $2 BILLION RECOVERED</li>
    <li>25 + YEAR OF LEGAL EXPERIENCE</li>
    <li>ATTORNEYS EXPEDITE QUICK PAYMENTS</li>
  </ul>

  <h2 class="heading" style="left:70px; top:592px;">HELP WITH VETERAN BENEFITS</h2>
  <p class="veteran-text">Veterans who have been diagnosed with mesothelioma can access a range of VA benefits. These benefits include monthly financial assistance of $3,800 or more to cover living expenses, which is available to both veterans and their families. Call us to discuss your options.</p>
  <div class="veteran-photo-shadow"></div>
  <div class="veteran-photo" role="img" aria-label="Two navy sailors in white caps saluting by the water, seen from behind"></div>

  <h2 class="heading" style="left:70px; top:734px;">MESOTHELIOMA CLIENT RECOVERIES</h2>
  <p class="recoveries-note">after Attorneys Fees &amp; Expenses :</p>

  <div class="results-band"></div>
  <table class="results">
    <colgroup><col style="width:249px"><col style="width:260px"><col style="width:269px"></colgroup>
    <tr>
      <td><span class="amount">$4,750,000</span><span class="source">NAVY EXPOSURE</span></td>
      <td><span class="amount">$3,310,650</span><span class="source">HVAC EXPOSURE</span></td>
      <td><span class="amount">$ 3,185,280</span><span class="source">PAPER MILL / CARPENTRY</span></td>
    </tr>
    <tr>
      <td><span class="amount">$2,715,915</span><span class="source">MECHANICS EXPOSURE</span></td>
      <td><span class="amount">$1,886,58</span><span class="source">WIFE EXPOSED WASHING<br>HUSBANDS’ CLOTHING</span></td>
      <td><span class="amount">$1,178,100</span><span class="source">R&amp;H TALC BABY POWDER</span></td>
    </tr>
  </table>

  <footer class="footer">
    <div class="footer-flag" role="img" aria-label="Faint American flag in the background"></div>
  </footer>
  <p class="promise"><strong>No Legal Fees unless You Win!</strong> We Get You Fair And Just Compensation From the Negligent Asbestos Product Manufacturers.</p>
  <div class="call-now">
    <svg viewBox="0 0 24 24" aria-hidden="true"><path fill="#fff" d="M6.6 10.8a15.1 15.1 0 0 0 6.6 6.6l2.2-2.2a1 1 0 0 1 1-.25 11.4 11.4 0 0 0 3.6.57 1 1 0 0 1 1 1V20a1 1 0 0 1-1 1A17 17 0 0 1 3 4a1 1 0 0 1 1-1h3.5a1 1 0 0 1 1 1c0 1.25.2 2.45.57 3.57a1 1 0 0 1-.25 1z"/><path fill="none" stroke="#fff" stroke-width="1.6" stroke-linecap="round" d="M14.5 3.5a6 6 0 0 1 6 6M14.5 6.8a2.8 2.8 0 0 1 2.7 2.7"/></svg>
    <span>Call Now <span class="number">1 800 555-0148</span></span>
  </div>
  <div class="consult-rule"></div>
  <p class="consult">Free Consultation</p>
  <p class="sponsor"><strong>Sponsor :</strong> Corbin Hale, Attorneys, Houston, TX</p>
</main>
</body>
</html>
```